Harbor Petroleum Business Cards

I would like to design some options for about 10 sets of double sided business cards for our team with a raised logo with a Silver glossy finished logo. We are a privately funded upstream Oil & Gas producer drilling vertical wells in Central Oklahoma with a long term production (ROI driven) strategy that we implement through an annual drilling program. We are focused on a shallow / vertical / long life / low decline strategy. We are based in downtown Tulsa Oklahoma. I have attached a sample business card and a picture of our hallway logo which we would like to replicate on the business cards.

Target Market(s)

SEC Accredited Investors and other Oil & Gas Operators

Industry/Entity Type

Upstream Oil & Gas

Contact Information for Business Card

You can see the sample photo attached, but email / website / address / direct phone / Cell Phone / Name / Title / Fax

Font styles to use
Other font styles liked:
• Felix Titling

Colors
0054AA
0677BA
7BADD7
CADEEF
E8F1F8

Requirements
Must have
• Glossy raised logo
Nice to have
• Possibly a new logo.
Should not have
• No Greens /

```html
<!DOCTYPE html>
<html lang="en">
<head>
<meta charset="utf-8">
<title>Harbor Petroleum Business Cards</title>
<link href="https://fonts.googleapis.com/css2?family=Lato:wght@400;700&display=swap" rel="stylesheet">
<style>
  :root {
    --backdrop: #2b2d31;
    --card: #1f1f20;
    --band: #7a7877;
    --band-text: #1c1c1c;
    --name-light: #8e8e8e;
    --name-bold: #b9b9b9;
    --muted: #7d7d7d;
    --mark: #9a9a9c;
    --icon-bg: #8a8a8a;
  }
  * { margin: 0; padding: 0; box-sizing: border-box; }
  html, body { width: 1200px; height: 952px; overflow: hidden; }
  body {
    background: var(--backdrop);
    font-family: "Lato", sans-serif;
    position: relative;
  }
  .card {
    position: absolute;
    width: 500px;
    height: 290px;
    background: var(--card);
    border-radius: 22px;
    overflow: hidden;
  }
  .card--front { left: 60px; top: 331px; }
  .card--back { left: 640px; top: 331px; }

  .wordmark {
    position: absolute;
    display: flex;
    align-items: center;
    gap: 12px;
    color: var(--mark);
    font-weight: 400;
    letter-spacing: 2px;
    text-transform: uppercase;
    white-space: nowrap;
  }
  .wordmark__dot {
    width: 26px; height: 26px;
    border-radius: 50%;
    background: var(--mark);
  }
  .card--front .wordmark { left: 130px; top: 58px; font-size: 20px; }
  .card--back .wordmark {
    left: 50%; top: 50%;
    transform: translate(-50%, -50%);
    font-size: 24px;
  }

  .person {
    position: absolute;
    right: 272px;
    top: 128px;
    text-align: right;
  }
  .person__name {
    font-size: 16px;
    letter-spacing: 0.5px;
    color: var(--name-light);
    text-transform: uppercase;
    white-space: nowrap;
  }
  .person__name strong { color: var(--name-bold); font-weight: 700; }
  .person__title { font-size: 12px; color: var(--muted); margin-top: 3px; }

  .contacts {
    position: absolute;
    left: 246px;
    top: 128px;
    list-style: none;
  }
  .contacts__item {
    display: flex;
    align-items: center;
    gap: 8px;
    font-size: 13px;
    color: var(--muted);
    height: 24px;
    white-space: nowrap;
  }
  .contacts__icon {
    width: 16px; height: 16px;
    border-radius: 3px;
    background: var(--icon-bg);
    display: flex; align-items: center; justify-content: center;
  }
  .contacts__icon svg { width: 11px; height: 11px; fill: var(--card); }

  .address-band {
    position: absolute;
    left: 0; right: 0; bottom: 38px;
    height: 30px;
    background: var(--band);
    color: var(--band-text);
    font-size: 13px;
    letter-spacing: 0.6px;
    display: flex;
    align-items: center;
    padding-left: 62px;
    white-space: nowrap;
  }
</style>
</head>
<body>
  <section class="card card--front" aria-label="Business card front">
    <div class="wordmark"><span class="wordmark__dot"></span>Harbor Petroleum, LLC</div>

    <div class="person">
      <p class="person__name">Daniel R. <strong>Whitford</strong></p>
      <p class="person__title">Managing Director</p>
    </div>

    <ul class="contacts">
      <li class="contacts__item">
        <span class="contacts__icon"><svg viewBox="0 0 24 24"><path d="M6.6 10.8a15.1 15.1 0 0 0 6.6 6.6l2.2-2.2a1 1 0 0 1 1-.25 11.4 11.4 0 0 0 3.6.57 1 1 0 0 1 1 1V20a1 1 0 0 1-1 1A17 17 0 0 1 3 4a1 1 0 0 1 1-1h3.5a1 1 0 0 1 1 1c0 1.25.2 2.45.57 3.57a1 1 0 0 1-.25 1z"/></svg></span>
        +1 918 555 0142
      </li>
      <li class="contacts__item">
        <span class="contacts__icon"><svg viewBox="0 0 24 24"><path d="M2 5h20v14H2z M4 7v.5l8 5 8-5V7l-8 5z"/></svg></span>
        info@harborpetroleum.com
      </li>
      <li class="contacts__item">
        <span class="contacts__icon"><svg viewBox="0 0 24 24"><path d="M12 2a10 10 0 1 0 0 20 10 10 0 0 0 0-20zm0 3 4 9h-3v5h-2v-5H8z"/></svg></span>
        www.harborpetroleum.com
      </li>
    </ul>

    <div class="address-band">2150 Riverside Avenue Tulsa, OK 74103</div>
  </section>

  <section class="card card--back" aria-label="Business card back">
    <div class="wordmark"><span class="wordmark__dot"></span>Harbor Petroleum, LLC</div>
  </section>
</body>
</html>
```